Flyer to promote new Commercial HVAC Preventative Maintenance clients

This flyer will be in the body of emails that will be sent to new, existing, and/or potential commericial buildings HVAC clients. It will have the least amount of words used, but it will convey the point with pertinent pictorial and graphics. It will show the value of a Periodic/Preventative routine maintenance to lower operating costs of their commericial buildings (i.e. office, medical, shopping centers, apartment, warehouse facility, etc.), in the following ways:
1) Reduce monthly power usage,
2) Reduce emergency HVAC service calls,
3) Reduce costly repairs costs,
4) Reduce HVAC down-times and angry tenants,
5) Increases the life expectancy of the existing and/or new HVAC equipment in the building and/or the equipment's' early replacement costs,
6) Reduces tenant's early termination of their lease and law suits against the landlords,
7) Increases tenant's renewal of the lease and agree to pay the increase rental rates,
8) Reduces unhappy customers and increases tenant's productivity,
9) By reducing the landlord's expenses, the value of the property will increase considerably and profitable to sell their holdings, or refinance and keep their holdings with an increased ROI (Return On Investment).

Landlords can not depend on their tenants' obligation to maintain the landlords' major assets, which is their HVAC equipment and systems.

With the periodic maintenance done by one reliable and licensed HVAC company, the will not use different companies that may or may not do the right repair job on their unit and hurt their bottom line and increase HVAC replacement COSTLY rates.

```html
<!DOCTYPE html>
<html lang="en">
<head>
<meta charset="utf-8">
<title>Commercial HVAC Preventative Maintenance</title>
<link href="https://fonts.googleapis.com/css2?family=Poppins:ital,wght@0,400;0,600;0,700;0,800;1,500&display=swap" rel="stylesheet">
<style>
  :root {
    --charcoal: #33363b;
    --orange: #f07a12;
    --amber: #f59a1c;
    --white: #ffffff;
    --body-text: #d4d6d9;
  }
  * { margin: 0; padding: 0; box-sizing: border-box; }
  html, body { width: 848px; height: 1200px; overflow: hidden; background: var(--charcoal); }
  .flyer {
    position: relative; width: 848px; height: 1200px; overflow: hidden;
    background: var(--charcoal); font-family: 'Poppins', sans-serif; color: var(--white);
  }
  .hero { position: absolute; left: 0; top: 0; width: 848px; height: 440px; }
  .brand {
    position: absolute; right: 44px; top: 38px; font-size: 33px; font-weight: 700;
    letter-spacing: -0.5px; color: var(--white);
  }
  .badge { position: absolute; left: 102px; top: 308px; width: 138px; height: 122px; }
  .headline { font-weight: 700; }
  .headline span {
    position: absolute; right: 29px; line-height: 1; white-space: nowrap; display: block;
  }
  .headline .line-a { top: 382px; font-size: 39.5px; }
  .headline .line-b {
    top: 422px; font-size: 48.4px; color: var(--orange);
    background: linear-gradient(90deg, var(--amber), var(--orange));
    -webkit-background-clip: text; background-clip: text; -webkit-text-fill-color: transparent;
  }
  .headline .line-c { top: 474px; font-size: 39.6px; }
  .copy {
    position: absolute; left: 30px; width: 788px; font-size: 16.4px; line-height: 20.5px;
    color: var(--body-text);
  }
  .copy .row { display: block; white-space: nowrap; text-align: justify; text-align-last: justify; }
  .copy .row.last { text-align-last: left; }
  .pill {
    position: absolute; left: 237px; top: 603px; width: 374px; height: 34px; border-radius: 17px;
    background: linear-gradient(90deg, var(--orange), var(--amber) 50%, var(--orange));
    text-align: center; font-size: 23px; font-weight: 700; line-height: 35px;
  }
  .benefit { position: absolute; display: flex; align-items: flex-start; gap: 9px; }
  .benefit .icon { flex: none; width: 32px; height: 32px; margin-top: -4px; }
  .benefit p { font-size: 19px; line-height: 23px; color: var(--body-text); }
  .benefit p span { display: block; white-space: nowrap; }
  .col-left { left: 13px; }
  .col-right { left: 442px; }
</style>
</head>
<body>
<main class="flyer">
  <svg class="hero" viewBox="0 0 848 440">
    <defs>
      <linearGradient id="photoTone" x1="0" y1="0" x2="1" y2="1">
        <stop offset="0" stop-color="#e6e7ea"/>
        <stop offset="0.55" stop-color="#b9bcc2"/>
        <stop offset="1" stop-color="#8d9097"/>
      </linearGradient>
      <linearGradient id="stripeTone" x1="0" y1="0" x2="1" y2="0">
        <stop offset="0" stop-color="#f59a1c"/>
        <stop offset="1" stop-color="#f07a12"/>
      </linearGradient>
    </defs>
    <path role="img" aria-label="Photo of two HVAC technicians in hard hats fitting a ceiling duct panel"
          d="M0 0 H848 V286 L347 381 L345 339 L0 426 Z" fill="url(#photoTone)"/>
    <path d="M0 426 L345 339 L347 381 L848 286" fill="none" stroke="url(#stripeTone)" stroke-width="6"/>
  </svg>

  <div class="brand">LOGO</div>

  <svg class="badge" viewBox="0 0 138 122">
    <defs>
      <linearGradient id="badgeTone" x1="0" y1="0" x2="0" y2="1">
        <stop offset="0" stop-color="#f59a1c"/>
        <stop offset="1" stop-color="#f07a12"/>
      </linearGradient>
    </defs>
    <path d="M69 4 Q74 4 77 10 L133 108 Q136 118 126 118 L12 118 Q2 118 5 108 L61 10 Q64 4 69 4 Z"
          fill="url(#badgeTone)" stroke="#ffffff" stroke-width="2.5"/>
    <text x="69" y="76" text-anchor="middle" font-family="Poppins, sans-serif" font-size="48" font-weight="400" fill="#fff" letter-spacing="-4">24</text>
    <text x="60" y="94" text-anchor="middle" font-family="Poppins, sans-serif" font-size="14" font-weight="700" fill="#fff">HOURS</text>
    <line x1="35" y1="98" x2="108" y2="98" stroke="#fff" stroke-width="1"/>
    <text x="70" y="108" text-anchor="middle" font-family="Poppins, sans-serif" font-size="8.5" font-style="italic" font-weight="500" fill="#fff">STAFF AVAILABLE</text>
  </svg>

  <h1 class="headline">
    <span class="line-a">NEW COMMERCIAL</span>
    <span class="line-b">HVAC PREVENTATIVE</span>
    <span class="line-c">MAINTENANCE</span>
  </h1>

  <p class="copy" style="top:531px;">
    <span class="row">It will show the value of a Periodic/Preventative routine maintenance to lower operating costs</span>
    <span class="row">of their commericial buildings (i.e. office, medical, shopping centers,apartment, warehouse</span>
    <span class="row last">facility, etc.), in the following ways:</span>
  </p>

  <div class="pill">lower operating costs</div>

  <div class="benefit col-left" style="top:666px;">
    <svg class="icon" viewBox="0 0 32 32"><circle cx="16" cy="16" r="14.5" fill="none" stroke="#f07a12" stroke-width="1.5"/><path d="M11 9v6l5 5 5-5V9M16 20v5" fill="none" stroke="#fff" stroke-width="1.3"/></svg>
    <p><span>Reduce monthly power usage</span></p>
  </div>
  <div class="benefit col-left" style="top:713px;">
    <svg class="icon" viewBox="0 0 32 32"><circle cx="16" cy="16" r="14.5" fill="none" stroke="#f07a12" stroke-width="1.5"/><circle cx="16" cy="12" r="4" fill="none" stroke="#fff" stroke-width="1.3"/><path d="M9 24c0-4 3-6 7-6s7 2 7 6" fill="none" stroke="#fff" stroke-width="1.3"/></svg>
    <p><span>Reduce emergency HVAC service</span><span>calls</span></p>
  </div>
  <div class="benefit col-left" style="top:781px;">
    <svg class="icon" viewBox="0 0 32 32"><circle cx="16" cy="16" r="14.5" fill="none" stroke="#f07a12" stroke-width="1.5"/><circle cx="14" cy="15" r="5" fill="none" stroke="#fff" stroke-width="1.6"/><circle cx="21" cy="21" r="3" fill="#fff"/></svg>
    <p><span>Reduce costly repairs costs</span></p>
  </div>
  <div class="benefit col-left" style="top:827px;">
    <svg class="icon" viewBox="0 0 32 32"><circle cx="16" cy="16" r="14.5" fill="none" stroke="#f07a12" stroke-width="1.5"/><rect x="12" y="9" width="8" height="15" rx="1.5" fill="none" stroke="#fff" stroke-width="1.3"/><path d="M14 14h4M14 17h4M14 20h4" stroke="#fff" stroke-width="1.2"/></svg>
    <p><span>Reduce HVAC down-times and</span><span>angry tenants</span></p>
  </div>
  <div class="benefit col-left" style="top:896px;">
    <svg class="icon" viewBox="0 0 32 32"><circle cx="16" cy="16" r="14.5" fill="none" stroke="#f07a12" stroke-width="1.5"/><path d="M8 22l4-5 4 3M24 22l-4-5-4 3M16 8v6" fill="none" stroke="#fff" stroke-width="1.3"/></svg>
    <p><span>Increases the life expectancy of the</span><span>existing and/or new HVAC equipment</span><span>in the building</span></p>
  </div>

  <div class="benefit col-right" style="top:662px;">
    <svg class="icon" viewBox="0 0 32 32"><circle cx="16" cy="16" r="14.5" fill="none" stroke="#f07a12" stroke-width="1.5"/><rect x="11" y="8" width="10" height="15" rx="1" fill="none" stroke="#fff" stroke-width="1.3"/><path d="M13 12h6M13 15h6M13 18h4" stroke="#fff" stroke-width="1.2"/></svg>
    <p><span>Reduces tenant's early termination</span><span>of their lease and law suits against</span><span>the landlords</span></p>
  </div>
  <div class="benefit col-right" style="top:754px;">
    <svg class="icon" viewBox="0 0 32 32"><circle cx="16" cy="16" r="14.5" fill="none" stroke="#f07a12" stroke-width="1.5"/><circle cx="12" cy="14" r="3" fill="none" stroke="#fff" stroke-width="1.3"/><circle cx="21" cy="18" r="3" fill="none" stroke="#fff" stroke-width="1.3"/><path d="M7 23c1-3 3-4 5-4M26 25c-1-2-3-3-5-3" fill="none" stroke="#fff" stroke-width="1.3"/></svg>
    <p><span>Increases tenant's renewal of the</span><span>lease and agree to pay the increase</span><span>rental rates</span></p>
  </div>
  <div class="benefit col-right" style="top:846px;">
    <svg class="icon" viewBox="0 0 32 32"><circle cx="16" cy="16" r="14.5" fill="none" stroke="#f07a12" stroke-width="1.5"/><circle cx="18" cy="19" r="5" fill="none" stroke="#fff" stroke-width="1.3"/><path d="M18 16v3h2M9 20V12M12 17V10M15 13V8" fill="none" stroke="#fff" stroke-width="1.3"/></svg>
    <p><span>Reduces unhappy customers and</span><span>increases tenant's productivity</span></p>
  </div>
  <div class="benefit col-right" style="top:915px;">
    <svg class="icon" viewBox="0 0 32 32"><circle cx="16" cy="16" r="14.5" fill="none" stroke="#f07a12" stroke-width="1.5"/><path d="M9 15l7-6 7 6v9H9z" fill="none" stroke="#fff" stroke-width="1.3"/><path d="M12 21l3-3 2 2 3-4" fill="none" stroke="#fff" stroke-width="1.2"/></svg>
    <p><span>By reducing the landlord's expenses,</span><span>the value of the property will increase</span><span>considerably and profitable to sell</span><span>their holdings</span></p>
  </div>

  <p class="copy" style="top:1033px;">
    <span class="row">Landlords can not depend on their tenants' obligation to maintain the landlords' major</span>
    <span class="row last">assets, which is their HVAC equipment and systems.</span>
  </p>
  <p class="copy" style="top:1095px;">
    <span class="row">With the periodic maintenance done by one reliable and licensed HVAC company, the will not</span>
    <span class="row">use different companies that may or may not do the right repair job on their unit and hurt</span>
    <span class="row last">their bottom line and increase HVAC replacement COSTLY rates.</span>
  </p>
</main>
</body>
</html>
```